Specialist Medical practice after professional trifold flyer design for patient information brochure

I am the Director of the Hollowbrook Clinic, a specialist medial and surgical practice in Australia. I am after a professional design of a patient information trifold flyer that can be used for web distribution or for commercial printing for upcoming educational event. The design would need to allow change of images and text to be used as template for future topics but have a common brand look across them. Colours would follow the logo, but primarily blue colours for the hollowbrook theme. The inside text needs to be clearly contrasted to the background for easy reading, as often elderly patients. The design would make use of curves or circles, but open for hexagonal, triangle square vector components. I have included an outline for the initial brochure and included images to include. Other stock background images can be used if they increase the impact of the design over included. A winning design is also one that could be modified to a 4 page bi-fold brochure

Target Market(s)

This will be provided to patients in GP practices, podiatry clinics, radiological practices. Aimed at patients to read and be compelled to look to site or get consultation with me

Industry/Entity Type

Medical

Font styles to use
Serif
Sans Serif

Colors
33a6d7
0355a3
86cfc6
cedeed
0292cd
85cae6

Requirements
Must have
• The front cover needs to engage the patient to pick up and read- yes I have a painful ankle and want to find out more. the goal for the inside is to provide the options but be able to direct to website for more info - website currently undergoing upgrade. After professional modern look. Not bright contrasting colours like many advertising brochures. Needs to able to have images and text changed but following same look to create new topics
Nice to have
• The focus is a Tri-fold brochure. Nice to be able to modify to bifold. A winning design would even offer both, or submit separate bifold and trifold. I am open to different versions of similar look. (eg option of brochure with curved elements, triangular or square, or hexagonal.
Should not have
• To many contrasting colours. Text must be easily read on background, either white or coloured background texture with transparency

```html
<!DOCTYPE html>
<html lang="en">
<head>
<meta charset="utf-8">
<title>Hollowbrook Clinic – Solutions for Ankle Arthritis Trifold</title>
<link rel="stylesheet" href="https://fonts.googleapis.com/css2?family=Montserrat:wght@300;400;600;700;800;900&display=swap">
<style>
  :root{
    --sky-blue:#33a6d7;
    --deep-blue:#0355a3;
    --teal:#86cfc6;
    --mist:#cedeed;
    --ocean:#0292cd;
    --pale-blue:#85cae6;
    --navy:#0b1a3a;
    --ink:#1b3553;
    --stage:#8c8c8c;
    --white:#ffffff;
  }
  *{box-sizing:border-box;margin:0;padding:0}
  html,body{width:1200px;height:1200px;overflow:hidden}
  body{background:var(--stage);font-family:"Montserrat",Arial,sans-serif;position:relative}
  .sheet{position:absolute;left:222px;width:742px;height:528px;overflow:hidden;box-shadow:0 3px 10px rgba(0,0,0,.35)}
  .sheet--outside{top:45px}
  .sheet--inside{top:610px}
  .sheet svg.art{position:absolute;inset:0;width:742px;height:528px}
  .block{position:absolute}

  /* outside */
  .bio{left:14px;top:13px;width:222px;font-size:12.4px;font-weight:300;line-height:1.24;color:var(--ocean);text-align:justify}
  .conditions{left:14px;top:170px;width:224px;font-size:8.2px;font-weight:300;line-height:1.3;color:var(--deep-blue)}
  .conditions h3{font-size:8.6px;font-weight:700;margin-bottom:2px}
  .conditions p{margin-bottom:5px}
  .brand{left:262px;top:36px;width:220px}
  .brand__name{font-size:15.5px;font-weight:800;color:var(--deep-blue);letter-spacing:.3px;display:flex;align-items:center;gap:6px}
  .brand__dot{width:12px;height:12px;border-radius:50%;background:var(--ocean);display:inline-block}
  .brand__tag{font-size:5.6px;color:var(--deep-blue);letter-spacing:.8px;margin:2px 0 0 18px}
  .contact{left:256px;top:83px;width:160px;font-size:6.3px;line-height:1.3;color:var(--ink)}
  .contact p{margin-bottom:7px}
  .badge{left:632px;top:116px;width:96px;text-align:center;font-size:15px;font-weight:900;line-height:1.25;color:var(--white)}
  .headline{left:592px;top:243px;width:150px;text-align:center;font-size:19px;font-weight:900;line-height:1.22;color:var(--deep-blue)}
  .nameplate{top:479px;color:var(--white)}
  .nameplate strong{display:block;font-size:15.5px;font-weight:800;letter-spacing:-.2px}
  .nameplate span{display:block;font-size:7.6px;font-weight:300;margin-top:1px}
  .nameplate--left{left:62px;width:180px;text-align:right}
  .nameplate--right{left:494px;width:180px}

  /* inside */
  .intro{left:18px;top:20px;width:229px;font-size:10.2px;font-weight:400;line-height:1.2;color:var(--white);text-align:justify}
  .body{font-size:7.5px;line-height:1.22;color:var(--white);text-align:justify}
  .body p{margin-bottom:7px}
  .lead{left:256px;top:22px;width:116px}
  .decision{left:256px;top:160px;width:238px}
  .fusion{left:256px;top:226px;width:238px}
  .replacement{left:256px;top:364px;width:238px}
  .results{left:502px;top:203px;width:220px}
  .label{display:inline-block;background:#0e5fb8;color:var(--white);font-size:7.4px;padding:2px 4px;margin-bottom:7px}
  .label--results{position:absolute;left:498px;top:182px}
</style>
</head>
<body>

<!-- Outside spread -->
<section class="sheet sheet--outside">
  <svg class="art" viewBox="0 0 742 528" aria-hidden="false">
    <defs>
      <linearGradient id="coast" x1="0" y1="0" x2="0" y2="1">
        <stop offset="0" stop-color="#e6eff3"/>
        <stop offset=".35" stop-color="#a9c7d3"/>
        <stop offset=".6" stop-color="#5f8e9c"/>
        <stop offset="1" stop-color="#7d8b5b"/>
      </linearGradient>
      <linearGradient id="sunfield" x1="0" y1="0" x2="0" y2="1">
        <stop offset="0" stop-color="#f4d08c"/>
        <stop offset=".6" stop-color="#c7a866"/>
        <stop offset="1" stop-color="#8e9b5a"/>
      </linearGradient>
      <linearGradient id="xray" x1="0" y1="0" x2="1" y2="1">
        <stop offset="0" stop-color="#1a1a1a"/>
        <stop offset=".5" stop-color="#8a8a8a"/>
        <stop offset="1" stop-color="#2a2a2a"/>
      </linearGradient>
      <linearGradient id="building" x1="0" y1="0" x2="0" y2="1">
        <stop offset="0" stop-color="#e4ecf1"/>
        <stop offset=".6" stop-color="#c9d2d6"/>
        <stop offset="1" stop-color="#5d7653"/>
      </linearGradient>
      <linearGradient id="portrait" x1="0" y1="0" x2="0" y2="1">
        <stop offset="0" stop-color="#e9eef1"/>
        <stop offset=".55" stop-color="#c8b4a4"/>
        <stop offset="1" stop-color="#1f2835"/>
      </linearGradient>
      <linearGradient id="film" x1="0" y1="0" x2="1" y2="0">
        <stop offset="0" stop-color="#f4f6f8"/>
        <stop offset=".5" stop-color="#6f8aa6"/>
        <stop offset="1" stop-color="#eef2f5"/>
      </linearGradient>
    </defs>

    <!-- panel backgrounds -->
    <rect x="0" y="0" width="245" height="528" fill="var(--mist)"/>
    <rect x="245" y="0" width="245" height="528" fill="url(#coast)" role="img" aria-label="Coastal headland and sea photograph"/>
    <rect x="490" y="0" width="252" height="528" fill="var(--teal)"/>
    <polygon points="490,0 742,0 742,150 640,195 560,220 490,230" fill="url(#sunfield)" role="img" aria-label="Photograph of a runner holding a painful ankle"/>

    <!-- wave -->
    <path d="M0,440 C100,470 200,470 270,430 S420,250 490,225 S660,170 742,150 L742,528 L0,528 Z" fill="var(--teal)"/>
    <path d="M0,440 C100,470 200,470 270,430 S420,250 490,225 S660,170 742,150" fill="none" stroke="var(--pale-blue)" stroke-width="14"/>
    <path d="M0,452 C100,482 205,480 278,440 S425,262 495,238 S665,180 742,162" fill="none" stroke="var(--ocean)" stroke-width="7"/>

    <!-- hexagon photos -->
    <polygon points="245,430 343,403 442,430 442,528 245,528" fill="url(#building)" role="img" aria-label="Hospital building photograph"/>
    <polygon points="432,200 550,200 609,303 550,406 432,406 373,303" fill="url(#xray)" role="img" aria-label="X-ray of an ankle with fusion plate and screws"/>
    <polygon points="596,378 742,378 742,528 560,528 524,455" fill="url(#film)" role="img" aria-label="Photograph of a doctor holding an ankle x-ray"/>
    <polygon points="192,327 244,357 244,417 192,447 140,417 140,357" fill="url(#portrait)" stroke="var(--deep-blue)" stroke-width="2" role="img" aria-label="Portrait photograph of the surgeon"/>
    <polygon points="680,88 724,113 724,163 680,188 636,163 636,113" fill="var(--deep-blue)" stroke="var(--pale-blue)" stroke-width="2"/>

    <!-- name plates -->
    <polygon points="64,477 245,477 245,515 50,515" fill="var(--deep-blue)"/>
    <polygon points="490,477 670,477 682,496 670,515 490,515" fill="var(--deep-blue)"/>
  </svg>

  <p class="block bio">Dr Andrew Callister is an Australian trained Orthopaedic Surgeon who has a primary focus in the treatment of conditions of the foot and ankle. He has completed post fellowship training in Foot and Ankle surgery both locally and internationally, and continues to update himself in the latest techniques.</p>

  <div class="block conditions">
    <h3>Conditions treated:</h3>
    <p>Dr Callister provides assessment and treatment of all foot and ankle conditions. He has special interest in the following:</p>
    <p>• Minimally invasive treatment for bunions and toe deformities.</p>
    <p>• Joint sparing procedures for arthritis or deformity, including the Flexa cartilage implant.</p>
    <p>• Joint fusion procedures for arthritis of the feet and ankle.</p>
    <p>• Sports injuries and tendinopathies.</p>
    <p>• Total ankle replacement and deformity correction of the foot and ankle.</p>
  </div>

  <div class="block brand">
    <div class="brand__name"><span class="brand__dot"></span>HOLLOWBROOK CLINIC</div>
    <div class="brand__tag">MEDICAL &amp; SURGICAL SPECIALISTS</div>
  </div>

  <div class="block contact">
    <p>LOCATIONS:</p>
    <p>- SUITE 402, LEVEL 4<br>HARBOURVIEW PRIVATE HOSPITAL<br>118-120 MARLIN ST<br>KESTREL BAY NSW</p>
    <p>- 42 FERRY LANE<br>TALLOWOOD NSW</p>
    <p>PHONE : (02) 5550 1234</p>
    <p>FAX : (02) 5550 1235</p>
    <p>WEBSITE : www.hollowbrookclinic.com.au</p>
    <p>EMAIL : info@hollowbrookclinic.com.au</p>
  </div>

  <div class="block badge">PAINFUL<br>ANKLE ?</div>
  <h1 class="block headline">SOLUTIONS<br>FOR<br>ANKLE-<br>ARTHRITIS</h1>

  <div class="block nameplate nameplate--left"><strong>DR ANDREW CALLISTER</strong><span>MBBS (HONS), FRACS (ORTHO), FA (ORTHO)</span></div>
  <div class="block nameplate nameplate--right"><strong>DR ANDREW CALLISTER</strong><span>ORTHOPAEDIC FOOT AND ANKLE SURGEON</span></div>
</section>

<!-- Inside spread -->
<section class="sheet sheet--inside">
  <svg class="art" viewBox="0 0 742 528">
    <defs>
      <linearGradient id="deep" x1="0" y1="0" x2="1" y2="1">
        <stop offset="0" stop-color="#0a1633"/>
        <stop offset=".5" stop-color="#0c2a66"/>
        <stop offset="1" stop-color="#0d4fa8"/>
      </linearGradient>
      <linearGradient id="xray2" x1="0" y1="0" x2="1" y2="1">
        <stop offset="0" stop-color="#0d0d0d"/>
        <stop offset=".55" stop-color="#8d8d8d"/>
        <stop offset="1" stop-color="#1c1c1c"/>
      </linearGradient>
      <linearGradient id="desk" x1="0" y1="0" x2="1" y2="1">
        <stop offset="0" stop-color="#e4f1f8"/>
        <stop offset="1" stop-color="#6fa7cf"/>
      </linearGradient>
    </defs>
    <rect width="742" height="528" fill="url(#deep)"/>
    <rect width="250" height="528" fill="#0a1838"/>
    <polygon points="130,210 230,210 280,300 230,390 130,390 80,300" fill="#123a7a" opacity=".7"/>
    <polygon points="440,60 600,60 680,200 600,340 440,340 360,200" fill="#1560c0" opacity=".25"/>
    <polygon points="300,330 470,330 550,470 470,610 300,610 220,470" fill="#1a6bd0" opacity=".3"/>
    <polygon points="0,240 200,240 250,380 170,528 0,528" fill="url(#xray2)" role="img" aria-label="Lateral x-ray of an arthritic ankle"/>
    <polygon points="380,0 500,0 530,80 480,158 380,158 345,80" fill="url(#xray2)" role="img" aria-label="X-ray of an ankle fusion with plate"/>
    <polygon points="575,0 742,0 742,182 600,182 546,90" fill="url(#desk)" role="img" aria-label="Stethoscope resting on a keyboard photograph"/>
    <polygon points="610,334 742,334 742,528 610,528 546,430" fill="url(#xray2)" role="img" aria-label="X-ray of a total ankle replacement implant"/>
  </svg>

  <div class="block intro">
    <p>Ankle arthritis is a painful condition where there is loss of cartilage from the ankle joint surface. Although not as common as knee or hip arthritis, pain can be debilitating affecting quality of life.</p>
    <p>Arthritis of the joint can be caused by trauma joint such as fracture or recurrent instability or secondary from inflammatory conditions such as rheumatoid arthritis.</p>
    <p>Pain from the joint will occur with activity causing a limp, limiting walking speed and distance. Often there is swelling of the joint with progressive loss of motion.</p>
    <p>Diagnosis is made with examination of the ankle and weight bearing x-rays showing loss of joint space.</p>
  </div>

  <p class="block body lead">When pain medication, activity modification and shoe ware modification is no longer effective to control the pain then it is worthwhile discussing with your GP for referral to Dr Andrew Callister for an opinion on further treatment. As an Orthopaedic Foot and Ankle surgeon, he will be able to assess your conditions and give advice on the best options for your treatment.</p>

  <p class="block body decision">The decision on the best option is based on your age, activity level, existing medical problems, previous ankle treatment and your expected outcome from treatment. In the situation of end stage arthritis options consist of either Ankle fusion or Total Ankle replacement.</p>

  <div class="block body fusion">
    <span class="label">Ankle Fusion Surgery</span>
    <p>This operation aims to stiffen the ankle joint by fusing the tibia and talus together in the optimal position for function. The common thought is that there will be no movement of the foot, and the patient will walk with a limp. The fusion only occurs at the ankle joint, leaving motion available to the surrounding joints. Although there is decreased motion, you will walk more normally after a fusion without a limp as the pain to the joint is removed.</p>
    <p>For more information on ankle fusion, risks and recovery visit our website :<br>www.hollowbrookclinic.com.au/Ankle-Fusion</p>
  </div>

  <div class="block body replacement">
    <span class="label">Total Ankle Replacement Surgery</span>
    <p>In suitable patients there may be the option to maintain joint motion and perform a Total Ankle Replacement. Like a hip or knee replacement operation, the arthritic joint is removed and replaced with an artificial joint. Like an ankle fusion there will alleviation of the pain and limp with maintenance of the ankle joint motion. Recovery to walking post-surgery is often much sooner than with ankle fusion. Dr Andrew Callister is one of the few surgeons to have completed an international fellowship in ankle replacement surgery and has been performing the technique since 2008. He is currently performing the technique using the Meridian Total Ankle with Precision guides.</p>
    <p>For more information on ankle replacement, risks and recovery visit our website :<br>www.hollowbrookclinic.com.au/Ankle-Replacement</p>
  </div>

  <span class="label label--results">Results of surgery</span>
  <p class="block body results">Successful surgery in the suitable patient will help resolve the pain associated with the ankle arthritis. Ankle Fusion surgery is ideal for patients with heavy labour work, allowing them to return to previous activities. There may be the risk of arthritis to surrounding joints in the future, but often this occurs many years down the track. Results from Total Ankle replacement surgery have been improving over the years, but there is known risks of loosening, cyst formation or failure of the joint over time that can occur in some patients. It is important to have a opinion from an Orthopaedic Foot and Ankle Surgeon experienced in these procedures to determine which procedure will provide the best long term solution for you.</p>
</section>

</body>
</html>
```